Business Card for Quillmark Ledger - A cannabis publication for executives.

I'd like some business cards for Quillmark Ledger. The logo is done (great job!) and I need a card design I will use with PRINTLY. I made it a short project to allow time for printing before an event. These will be standard sized cards (final artwork size 3.66" x 2.16" at 300dpi) with a final card size of 3.5" x 2.0". (See PRINTLY.com if you need more info.) I might try rounded corners but am not sure yet. I think the design will work okay with rounded.

Quillmark Ledger will be a bi-weekly publication for the cannabis industry. It is targeted to investors and industry executives, not consumers or pot smokers. So our market is more B2B. However I am open to creativity and making the card something people remark on.

My contact for card:

Dana Merrow
Founder/CEO
dana@quillmarkledger.example

2740 Harlow Avenue
Boston MA 02135
(617)555-0194

Target Market(s)

Executives, Industry people and investors in the Cannabis sector.

Contact Information for Business Card

PRINTLY does do double sided and the second side can be the same or different images. Only one side is required but use of the second side would be a bonus.

Font styles to use
Serif
Sans Serif
Decorative

Colors

Designer to choose colors to be used in the design.

Requirements
Must have
• Logo, contact info
Nice to have
• Style and design to make the card stand out in a crowd.

```html
<!DOCTYPE html>
<html lang="en">
<head>
<meta charset="utf-8">
<title>Quillmark Ledger — Business Card</title>
<link href="https://fonts.googleapis.com/css2?family=Marcellus&family=Source+Sans+3:wght@300;400;700&display=swap" rel="stylesheet">
<style>
  :root {
    --backdrop: #d6e0e3;
    --card-white: #ffffff;
    --teal-deep: #01465e;
    --plum-deep: #372152;
    --gold: #d6bd86;
    --slate-grey: #95979b;
    --ink-white: #ffffff;
  }
  * { margin: 0; padding: 0; box-sizing: border-box; }
  html, body {
    width: 1200px; height: 1000px; overflow: hidden;
    background: var(--backdrop);
  }
  .canvas { position: relative; width: 1200px; height: 1000px; }

  .card {
    position: absolute;
    background: var(--card-white);
  }
  .card-front { left: 163px; top: 44px; width: 658px; height: 396px; }
  .card-back  { left: 367px; top: 532px; width: 666px; height: 400px; }

  .front-panel {
    position: absolute; left: 43px; top: 44px; width: 571px; height: 307px;
    background: linear-gradient(90deg, var(--teal-deep) 0%, var(--teal-deep) 22%, var(--plum-deep) 100%);
    display: flex; align-items: center; justify-content: center; gap: 18px;
  }
  .brand-square {
    width: 38px; height: 38px; background: var(--gold);
  }
  .brand-name {
    font-family: "Marcellus", serif;
    font-size: 46px; color: var(--gold);
    white-space: nowrap; letter-spacing: 0.5px;
  }

  .back-panel {
    position: absolute; left: 44px; top: 45px; width: 578px; height: 310px;
    background: var(--slate-grey);
    color: var(--ink-white);
    font-family: "Source Sans 3", sans-serif;
  }
  .holder-name {
    position: absolute; top: 68px; left: 0; width: 100%;
    text-align: center; font-size: 28px; letter-spacing: 5px;
  }
  .holder-name .given { font-weight: 300; }
  .holder-name .family { font-weight: 700; }
  .holder-role {
    position: absolute; top: 108px; left: 14px; right: 16px;
    display: flex; align-items: center; gap: 14px;
    font-size: 18px; font-weight: 400;
  }
  .holder-role .rule { flex: 1; height: 2px; background: var(--ink-white); }
  .contact-list {
    position: absolute; left: 46px; top: 160px; list-style: none;
  }
  .contact-item {
    display: flex; align-items: center; height: 39px;
    font-size: 18px; font-weight: 400;
  }
  .contact-icon { width: 26px; height: 22px; margin-right: 18px; fill: var(--ink-white); }
</style>
</head>
<body>
<main class="canvas">
  <section class="card card-front" aria-label="Card front">
    <div class="front-panel">
      <span class="brand-square"></span>
      <span class="brand-name">Quillmark Ledger</span>
    </div>
  </section>

  <section class="card card-back" aria-label="Card back">
    <div class="back-panel">
      <h1 class="holder-name"><span class="given">Dana</span> <span class="family">Merrow</span></h1>
      <div class="holder-role"><span class="rule"></span><span>Founder / CEO</span><span class="rule"></span></div>
      <ul class="contact-list">
        <li class="contact-item">
          <svg class="contact-icon" viewBox="0 0 26 22" aria-hidden="true">
            <path d="M1 4h24v14H1z M1 4l12 9 12-9" fill="none" stroke="#fff" stroke-width="0"/>
            <path d="M1 4h24L13 12z"/><path d="M1 6l12 8 12-8v12H1z"/>
          </svg>
          <span>dana@quillmarkledger.example</span>
        </li>
        <li class="contact-item">
          <svg class="contact-icon" viewBox="0 0 26 22" aria-hidden="true">
            <path d="M5 2l4 0 2 5-3 2c1 3 3 5 6 6l2-3 5 2v4c-10 1-17-6-16-16z"/>
          </svg>
          <span>2740 Harlow Avenue, Boston MA 02135</span>
        </li>
        <li class="contact-item">
          <svg class="contact-icon" viewBox="0 0 26 22" aria-hidden="true">
            <path d="M13 1L1 11h3v10h6v-6h6v6h6V11h3z"/>
          </svg>
          <span>(617)555-0194</span>
        </li>
      </ul>
    </div>
  </section>
</main>
</body>
</html>
```